K7 Website Project

We need a web design for our new company K7. We just decided on our company brand. I will upload our company brand for you to use in the web design. We want a powerful few statements to catch the eye of the browser. Our company is being founded to protect elementary schools, junior high schools and high schools against predators that want to harm children. We are going to employ veterans and police officers, only. Superintendents of schools, principals of schools will be viewing this site. This site needs to be thoughtful and impactful to the current needs of school districts. We will have a couple testimonials that will be included on the site.
Updates

We need this website as soon as possible.  We added more information.

Target Market(s)

School districts

Industry/Entity Type

School

Requirements
Must have
• Website must have logo and brand. Area for contact information. Links to take the user to learn more about the company, testimonials, frequently asked questions, contact information
Should not have
• Should not be too busy, simple but classy.

```html
<!DOCTYPE html>
<html lang="en">
<head>
<meta charset="utf-8">
<title>K7 — School Safety Professionals</title>
<link href="https://fonts.googleapis.com/css2?family=Arimo:wght@400;700&family=PT+Sans:wght@400;700&display=swap" rel="stylesheet">
<style>
:root{
  --black:#000;
  --gold:#c9a24a;
  --gold-light:#e8c871;
  --gold-dark:#8a6a1f;
  --gold-text:#e3b54a;
  --navy:#0d2a6e;
  --blue:#1a63b5;
  --panel:#141414;
  --grey:#8c8c8c;
  --white:#fff;
}
*{margin:0;padding:0;box-sizing:border-box}
html,body{width:1200px;height:1131px;overflow:hidden;background:var(--black)}
body{position:relative;font-family:"Arimo",Arial,sans-serif;color:var(--white)}
.abs{position:absolute}
.top-rule{left:0;top:0;width:1200px;height:4px;background:var(--gold)}
.brand{left:102px;top:40px;display:flex;align-items:center;gap:12px}
.brand-mark{width:40px;height:40px;background:var(--gold)}
.brand-name{font-family:"PT Sans",sans-serif;font-weight:700;font-size:56px;color:var(--gold-light);line-height:1}
.phone-icon{left:677px;top:45px;width:42px;height:42px;border-radius:50%;background:radial-gradient(circle at 40% 35%,#fff6c8,#c9a24a 55%,#7d6020);border:2px solid #ddd}
.phone{left:728px;top:50px;font-family:"PT Sans",sans-serif;font-size:25px;color:var(--white)}
.email{left:790px;top:82px;font-family:"PT Sans",sans-serif;font-size:15px;color:var(--gold-text);text-decoration:underline}
.social{top:51px;width:43px;height:43px;border-radius:5px;background:linear-gradient(#e2c07b,#9b7a3a)}
.nav{left:0;top:147px;width:1200px;height:58px;background:linear-gradient(#f0d891 0,#c9a24a 8%,#b08a36 55%,#8f6c22 100%);border-top:3px solid #f3dc93}
.nav ul{list-style:none;position:absolute;left:98px;top:0;display:flex;height:55px}
.nav li{font-family:"Arimo",sans-serif;font-weight:700;font-size:14px;letter-spacing:.5px;display:flex;align-items:center;justify-content:center;border-right:1px solid #d8b868;height:55px}
.nav li.active{background:linear-gradient(#a98230,#d3b060)}
.slider{left:96px;top:229px;width:1022px;height:402px;background:var(--grey)}
.slide{left:104px;top:238px;width:1006px;height:384px;background:linear-gradient(110deg,#2b3f7a 0%,#6d7fae 30%,#d9dbe4 50%,#b9bccb 65%,#f4f4f6 100%)}
.headline{left:104px;top:342px;width:436px;height:84px;background:rgba(220,228,245,.85);padding:2px 12px;font-family:"PT Sans",sans-serif;font-size:34px;line-height:40px}
.headline .l1{color:var(--navy)}
.headline .l2{color:#111}
.dots-bar{left:104px;top:585px;width:430px;height:37px;background:rgba(0,0,0,.45)}
.dot{top:594px;width:19px;height:19px;border-radius:50%;background:#b68a2a}
.dot.on{background:#f0e08e}
.contact-form{left:765px;top:247px;width:341px;height:364px}
.form-title{left:765px;top:278px;width:341px;text-align:center;font-family:"Arimo",sans-serif;font-weight:700;font-size:28px}
.label{width:80px;text-align:right;font-size:13px}
.field{left:854px;width:216px;background:#fff;border:1px solid #c9d3e6;border-radius:7px}
.submit{left:848px;top:573px;width:133px;height:38px;border-radius:18px;border:2px solid #fff;background:linear-gradient(#e8c45e,#9d7420);font-family:"PT Sans",sans-serif;font-weight:700;font-size:18px;letter-spacing:1px;display:flex;align-items:center;justify-content:center}
.section-tag{left:98px;top:663px}
.tag-text{left:104px;top:670px;font-family:"PT Sans",sans-serif;font-weight:700;font-size:22px;color:#fff}
.lead{left:99px;top:719px;width:660px;font-family:"PT Sans",sans-serif;font-weight:700;font-size:18px;line-height:22px;color:var(--gold-text)}
.photo-frame{left:101px;top:784px;width:203px;height:200px;background:#1c1c1c;border:1px solid #333}
.photo{left:108px;top:790px;width:190px;height:188px;background:linear-gradient(#d9d2c6,#1d2b3a 40%,#16202c 85%,#3a5060)}
.body-copy{left:318px;top:788px;width:474px;font-size:13.5px;line-height:21px}
.body-copy p+p{margin-top:21px}
.more{font-family:"Arimo",sans-serif;font-weight:700;font-size:12.5px;color:var(--gold-text)}
.testimonials{left:817px;top:667px;width:296px;height:345px;background:var(--panel);border:1px solid #333}
.testi-head{left:822px;top:671px;width:288px;height:43px;background:linear-gradient(#e7c468,#a07a28);font-family:"PT Sans",sans-serif;font-weight:700;font-size:22px;letter-spacing:.5px;padding:7px 11px}
.quote{font-family:"PT Sans",sans-serif;font-weight:700;font-size:32px;color:var(--gold-text);line-height:1}
.testi-copy{left:838px;top:740px;width:264px;font-size:13.5px;line-height:21px;text-align:justify}
.footer{left:0;top:1065px;width:1200px;height:66px;background:linear-gradient(#b08a34,#7a5c1a 40%,#c9a24a 100%)}
.copyright{left:93px;top:1091px;font-size:12.5px}
.footer-links{right:75px;top:1091px;font-size:13px;display:flex;gap:14px}
</style>
</head>
<body>
<div class="abs top-rule"></div>

<header>
  <div class="abs brand"><span class="brand-mark"></span><span class="brand-name">K7</span></div>
  <div class="abs phone-icon"></div>
  <div class="abs phone">(01) 5550 7142</div>
  <div class="abs email">Info@K7.com</div>
  <div class="abs social" style="left:999px"></div>
  <div class="abs social" style="left:1059px"></div>
</header>

<nav class="abs nav">
  <ul>
    <li class="active" style="width:103px">HOME</li>
    <li style="width:182px">ABOUT COMPANY</li>
    <li style="width:169px">TESTIMONIALS</li>
    <li style="width:92px">FAQ</li>
    <li style="width:120px;border-right:0">CONTACT US</li>
  </ul>
</nav>

<section>
  <div class="abs slider"></div>
  <div class="abs slide" role="img" aria-label="Photo of a uniformed officer shaking hands with an official in front of a small crowd"></div>
  <div class="abs headline"><div class="l1">Former police officers to be</div><div class="l2">hired by school districts</div></div>
  <div class="abs dots-bar"></div>
  <div class="abs dot" style="left:124px"></div>
  <div class="abs dot on" style="left:152px"></div>
  <div class="abs dot" style="left:180px"></div>

  <svg class="abs contact-form" viewBox="0 0 341 364" aria-hidden="true">
    <defs><linearGradient id="panelBlue" x1="0" y1="0" x2="0" y2="1"><stop offset="0" stop-color="#1b6bbd"/><stop offset="1" stop-color="#0b2466"/></linearGradient></defs>
    <path d="M8 16 L334 0 L341 0 L341 364 L0 331 L0 26 Q0 17 8 16 Z" fill="url(#panelBlue)"/>
  </svg>
  <div class="abs form-title">Contact Information</div>
  <div class="abs label" style="left:758px;top:350px">Name :</div>
  <div class="abs label" style="left:758px;top:388px">Email :</div>
  <div class="abs label" style="left:758px;top:425px">Phone :</div>
  <div class="abs label" style="left:758px;top:463px">Question :</div>
  <div class="abs field" style="top:345px;height:28px"></div>
  <div class="abs field" style="top:381px;height:28px"></div>
  <div class="abs field" style="top:417px;height:28px"></div>
  <div class="abs field" style="top:457px;height:91px"></div>
  <div class="abs submit">SUBMIT</div>
</section>

<main>
  <svg class="abs section-tag" width="285" height="42" viewBox="0 0 285 42" aria-hidden="true">
    <defs><linearGradient id="tagGold" x1="0" y1="0" x2="0" y2="1"><stop offset="0" stop-color="#e6c266"/><stop offset="1" stop-color="#946e20"/></linearGradient></defs>
    <path d="M2 2 L268 2 L283 21 L268 40 L2 40 Z" fill="url(#tagGold)" stroke="#fff" stroke-width="2"/>
  </svg>
  <div class="abs tag-text">What We Do ?</div>
  <div class="abs lead">We are training former servicemen/women and former police officers to be hired by school districts.</div>
  <div class="abs photo-frame"></div>
  <div class="abs photo" role="img" aria-label="Group photo of uniformed officers standing in a row"></div>
  <div class="abs body-copy">
    <p>Simply dummy text of the printing and typesetting industry. Lorem Ipsum has been the industry's standard dummy text ever since the 1500s, when an unknown printer took a galley of type and scrambled it to make a type specimen book. It has survived not only five centuries, but also the leap into electronic and scrambled it to make a type specimen book.</p>
    <p>Galley of type and scrambled it to make a type specimen book. It has survived not only five centuries, but also the leap into electronic and scrambled it to make a type specimen book.</p>
  </div>
  <div class="abs more" style="left:745px;top:988px">More[+]</div>

  <aside>
    <div class="abs testimonials"></div>
    <div class="abs testi-head">Testimonials</div>
    <div class="abs quote" style="left:819px;top:722px">&ldquo;</div>
    <div class="abs testi-copy">Simply dummy text of the printing and typesetting industry. Lorem Ipsum has been the industry's standard dummy text ever since the 1500s, when an unknown printer took a galley of type and scrambled it to make a type specimen book. It has survived not only five centuries, but also the leap into electronic and scrambled it to make a type specimen book. It has survived not only five centuries, but also the leap into electronic.</div>
    <div class="abs quote" style="left:986px;top:954px">&rdquo;</div>
    <div class="abs more" style="left:1054px;top:982px">More[+]</div>
  </aside>
</main>

<footer class="abs footer">
  <div class="abs copyright" style="top:26px">Copyright © 2013 K7 All Rights Reserved.</div>
  <div class="abs footer-links" style="top:26px"><span>About Company</span><span>|</span><span>Testimonials</span><span>|</span><span>FAQ</span><span>|</span><span>Contact us</span></div>
</footer>
</body>
</html>
```